依頼詳細
①TOPページのデザイン案をご提案ください。
②採用させていただく可能性の高い方と、
下層ページ1ページ、採用サイト等別サイト2ページ分について
ご相談したいと考えております。

<サイト概要>
・4ページ分(トップページ、下層ページ、採用サイト等2サイト)
・レスポンシブ
・セミナー案内などを、wordpressで更新していきます。

<納品物>
デザインカンプ(PSD希望ですが、AIでも可)を納品してください。

<応募条件>
・継続依頼も検討しているため、連絡がスムーズな方。

<参考サイト>
・株式会社ペネムス・ヤカルト
http://www.pnm-example.co.jp/

上記サイトのように、ファーストビューに背景に動画をフルスクリーンで表示させるのを希望しています。

・ツクリエ採用サイト
https://www.tsukurie-example.jp/saiyou/service/business.html

<提供する素材>
・写真、ロゴ、サイト内で使用するテキスト
サイトURL
http://www.meadowpath-x.com/
ページ数
4ページ
希望イメージ
シンプル 複雑
単色 カラフル
暗い 明るい
日常 高級
遊び心 厳粛
未来的 伝統的
女性的 男性的
希望する色
設定なし
納品ファイル
• イラストレーター形式 (.ai)
• フォトショップ形式 (.psd)
補足説明
・イラストレーター、フォトショップ、どちらで作成していただいても構いません。最終的に、制作データ(ai or psd)で納品をしていただける方。
・クライアント企業とのコミュニケーションに慣れていて、細かい修正等に対応していただける方
提供する素材を添付させていただきますので、
こちらをご使用ください。

<提供する素材>
・写真、ロゴ、サイト内で使用するテキスト
募集の締め切りを延長しましたので、
引き続きご提案をお待ちしております。
■ 選んだ理由

私たちのイメージに一番近いデザインを出していただきました。
またこちらの意向を汲んでくださり、
今後も引き続きお願いしたいと感じましたので決めさせていただきました。

■ 提案者全員のお礼・コメント

皆様、数々のご提案をいただき、ありがとうございました。

```html
<!DOCTYPE html>
<html lang="ja">
<head>
<meta charset="utf-8">
<title>Meadowpath | 歯科医院専門コンサルティング</title>
<link href="https://fonts.googleapis.com/css2?family=Noto+Sans+JP:wght@400;500;700&family=Noto+Serif+JP:wght@400;600&display=swap" rel="stylesheet">
<style>
:root{
  --purple:#8a6aa6;
  --purple-soft:#c9b3d8;
  --lavender:#f4ecf7;
  --lavender-deep:#e9dcef;
  --green:#78b83a;
  --ink:#3c3c3c;
  --muted:#8a8a8a;
  --line:#dcdcdc;
  --white:#ffffff;
  --photo-warm:#d9cfc4;
  --photo-cool:#cfd6dd;
}
*{box-sizing:border-box;margin:0;padding:0}
html,body{width:1200px;height:5120px;overflow:hidden}
body{font-family:"Noto Sans JP",sans-serif;color:var(--ink);background:var(--white);font-size:14px;line-height:1.8}
.serif{font-family:"Noto Serif JP",serif}
.photo{display:block}

/* header / hero */
.hero{position:relative;height:620px;background:linear-gradient(180deg,#e7e2dc 0%,#cfc6bb 55%,#b9ada0 100%)}
.hero .photo{position:absolute;inset:0}
.site-nav{position:absolute;top:40px;left:200px;display:flex;gap:36px;font-size:12px;color:var(--ink)}
.site-nav li{list-style:none;text-align:center;line-height:1.3}
.site-nav small{display:block;font-size:9px;color:var(--muted)}
.nav-right{left:760px}
.brand{position:absolute;top:18px;left:520px;display:flex;align-items:center;gap:10px;background:rgba(255,255,255,.9);padding:14px 22px}
.brand-mark{width:22px;height:22px;border-radius:50%;background:var(--green)}
.brand-name{font-size:24px;font-weight:700;color:var(--green);letter-spacing:.02em}
.tel-box{position:absolute;top:70px;left:820px;background:rgba(255,255,255,.92);padding:6px 16px;text-align:center}
.tel-box small{display:block;font-size:10px;color:var(--muted)}
.tel-box strong{font-size:26px;color:var(--purple);letter-spacing:.04em;display:flex;align-items:center;gap:8px}

.intro{position:relative;height:240px}
.intro-card{position:absolute;left:180px;top:40px;width:340px;height:180px;background:var(--green);color:var(--white);display:flex;align-items:center;justify-content:center;text-align:center;font-size:19px;line-height:1.8;margin-top:-20px}
.intro-text{position:absolute;left:600px;top:50px;width:560px;font-size:13px;color:var(--ink)}

.sec-head{text-align:center}
.sec-head small{display:block;font-size:10px;letter-spacing:.2em;color:var(--muted)}
.sec-head h2{font-family:"Noto Serif JP",serif;font-weight:600;font-size:22px;letter-spacing:.08em}
.sec-head h2::after{content:"";display:block;width:40px;height:1px;background:var(--purple);margin:10px auto 0}

/* voices */
.voices{height:340px;padding-top:30px}
.voice-strip{display:flex;margin-top:36px;height:150px}
.voice-strip .photo{flex:1;height:150px;border-right:2px solid var(--white);background:linear-gradient(180deg,#eceae7,#d6d1cb)}
.voice-strip .photo.on{background:linear-gradient(180deg,#7b756f,#4f4a45);position:relative}
.play{position:absolute;left:50%;top:50%;width:44px;height:44px;margin:-22px;border-radius:50%;background:rgba(255,255,255,.85);display:flex;align-items:center;justify-content:center}

/* services */
.services{height:1240px;background:var(--lavender);padding-top:80px}
.svc-grid{width:880px;margin:50px auto 0;background:var(--white)}
.svc-row{display:flex;height:310px}
.svc-row > *{flex:1}
.svc-text{padding:44px 48px}
.svc-text h3{font-family:"Noto Serif JP",serif;font-size:19px;font-weight:600;margin-bottom:14px}
.svc-text p{font-size:12px;color:var(--ink)}
.btn{display:inline-flex;align-items:center;justify-content:space-between;width:190px;height:38px;margin-top:26px;padding:0 18px;border:1px solid var(--purple);color:var(--purple);font-size:12px;text-decoration:none}
.btn-wide{width:220px}

/* blog */
.blog{height:520px;padding-top:80px}
.blog-list{display:flex;gap:12px;margin-top:36px;padding:0 8px}
.post{flex:1}
.post .photo{height:150px;background:linear-gradient(135deg,#e9e4df,#c9c1b8)}
.post p{font-size:11px;margin-top:10px;line-height:1.6}
.post a{display:block;font-size:10px;color:var(--purple);text-align:right;margin-top:4px}
.pager{display:flex;justify-content:center;gap:10px;margin-top:30px;align-items:center}
.pager span{width:8px;height:8px;border-radius:50%;background:var(--purple-soft)}
.pager span.on{background:var(--purple)}
.pager i{width:26px;height:26px;background:var(--purple);display:flex;align-items:center;justify-content:center}

/* recruit */
.recruit{position:relative;height:620px;background:linear-gradient(180deg,var(--lavender-deep),var(--lavender) 70%,#fbf8fc)}
.recruit .photo{position:absolute;right:0;top:0;width:420px;height:560px;background:linear-gradient(160deg,#e3d7e8,#bfb1c6 60%,#e9e2ec)}
.recruit-body{position:relative;width:640px;margin-left:170px;padding-top:60px;text-align:center}
.recruit-body .lead{font-family:"Noto Serif JP",serif;font-size:24px;margin:30px 0 26px;line-height:1.6}
.recruit-body .lead em{font-style:normal;color:var(--purple)}
.recruit-body p{font-size:12px}

/* message */
.message{position:relative;height:520px;background:var(--white)}
.message .photo{position:absolute;right:0;top:20px;width:620px;height:460px;background:linear-gradient(160deg,#f1f1f1,#cfd3d8 60%,#eef0f2)}
.message h2{position:absolute;left:250px;top:220px;font-family:"Noto Serif JP",serif;font-weight:400;font-size:26px;line-height:1.6}

/* map */
.map{height:640px;background:linear-gradient(135deg,#ecebe6,#dedcd4 50%,#e7e8e2);border-top:4px solid var(--purple);position:relative}
.map-pin{position:absolute;left:586px;top:280px}

/* footer */
.site-footer{height:360px;background:#fafafa;display:flex;padding:50px 70px;gap:50px;font-size:12px}
.foot-brand{display:flex;align-items:center;gap:8px;align-self:flex-end;margin-bottom:40px}
.foot-brand .brand-name{font-size:22px}
.foot-nav{display:flex;gap:40px;flex:1}
.foot-nav ul{list-style:none;line-height:2.1}
.foot-nav li.sub{color:var(--muted);font-size:11px}
.foot-addr{font-size:11px;color:var(--muted);text-align:right;align-self:flex-end;margin-bottom:40px}
</style>
</head>
<body>

<header class="hero">
  <div class="photo" role="img" aria-label="ハロウィン装飾の前でマイクを持って講演する男性と聴講者たちの写真"></div>
  <ul class="site-nav">
    <li><small>ABOUT</small>会社概要</li>
    <li><small>SERVICE</small>サービス</li>
    <li><small>VOICE</small>クライアントの声</li>
  </ul>
  <div class="brand"><span class="brand-mark"></span><span class="brand-name">Meadowpath</span></div>
  <ul class="site-nav nav-right">
    <li><small>SEMINAR</small>歯科塾</li>
    <li><small>BLOG</small>ブログ</li>
    <li><small>CONTACT</small>お問い合わせ</li>
  </ul>
  <div class="tel-box">
    <small>歯科医院専門コンサルティング</small>
    <strong><svg width="22" height="22" viewBox="0 0 24 24"><path fill="#8a6aa6" d="M6.6 10.8a15 15 0 0 0 6.6 6.6l2.2-2.2c.3-.3.7-.4 1-.2 1.1.4 2.3.6 3.6.6.6 0 1 .4 1 1V20c0 .6-.4 1-1 1A17 17 0 0 1 3 4c0-.6.4-1 1-1h3.5c.6 0 1 .4 1 1 0 1.3.2 2.5.6 3.6.1.3 0 .7-.2 1z"/></svg>0120-000-482</strong>
  </div>
</header>

<section class="intro">
  <div class="intro-card serif">クライアントの“こうしたい”に<br>“そこまでやるか”でカタチにする。</div>
  <p class="intro-text">私たちは歯科医院の経営に寄り添い、現場の声から生まれる課題を一つずつ丁寧に解決していきます。<br>開業から成長期まで、長く続く信頼関係を大切にしながら医院づくりをお手伝いしています。</p>
</section>

<section class="voices">
  <div class="sec-head"><small>VOICE</small><h2>クライアントの声</h2></div>
  <div class="voice-strip">
    <div class="photo" role="img" aria-label="クライアントの男性の写真"></div>
    <div class="photo on" role="img" aria-label="インタビュー動画のサムネイル"><span class="play"><svg width="16" height="16" viewBox="0 0 16 16"><path d="M4 2l10 6-10 6z" fill="#3c3c3c"/></svg></span></div>
    <div class="photo" role="img" aria-label="クライアントの男性の写真"></div>
    <div class="photo" role="img" aria-label="クライアントの男性の写真"></div>
    <div class="photo" role="img" aria-label="クライアントの男性の写真"></div>
    <div class="photo" role="img" aria-label="クライアントの男性の写真"></div>
    <div class="photo" role="img" aria-label="クライアントの男性の写真"></div>
  </div>
</section>

<section class="services">
  <div class="sec-head"><small>SERVICE</small><h2>サービス</h2></div>
  <div class="svc-grid">
    <div class="svc-row">
      <div class="svc-text">
        <h3>歯科医院専門コンサルティング</h3>
        <p>医院の集患、採用、人材育成、組織作りを支援します。<br>医院ごとの課題に合わせて、現場で成果につながる仕組みを提案します。</p>
        <a class="btn" href="#">詳細を見る<span>›</span></a>
      </div>
      <div class="photo" role="img" aria-label="スーツ姿の男性コンサルタントの写真" style="background:linear-gradient(135deg,#f2f2f2,#c9ccd1)"></div>
    </div>
    <div class="svc-row">
      <div class="photo" role="img" aria-label="書類にペンで書き込む手元の写真" style="background:linear-gradient(135deg,#d4d7dc,#a9adb4)"></div>
      <div class="svc-text">
        <h3>ホームページ作成</h3>
        <p>歯科医院専門の制作チームが、医院の強みを伝えるホームページを作成します。<br>公開後の更新や集患の改善までしっかり支えます。</p>
        <a class="btn" href="#">詳細を見る<span>›</span></a>
      </div>
    </div>
    <div class="svc-row">
      <div class="svc-text">
        <h3>歯科塾（歯科医療従事者のコミュニティ）</h3>
        <p>志を同じくする医院が集い、学び合うコミュニティです。<br>定期的な勉強会や交流会を通じて、経営と診療の質を高めていきます。</p>
        <a class="btn" href="#">詳細を見る<span>›</span></a>
      </div>
      <div class="photo" role="img" aria-label="並べられた歯科治療器具の写真" style="background:linear-gradient(135deg,#eef0f3,#b8bfc8)"></div>
    </div>
  </div>
</section>

<section class="blog">
  <div class="sec-head"><small>BLOG</small><h2>ブログ</h2></div>
  <div class="blog-list">
    <article class="post"><div class="photo" role="img" aria-label="医院で打ち合わせする様子の写真"></div><p>医院づくりの現場から、今月の取り組みをご紹介します。</p><a href="#">詳しくみる ›</a></article>
    <article class="post"><div class="photo" role="img" aria-label="笑顔の女性スタッフの写真"></div><p>スタッフ研修で大切にしている三つのことをお伝えします。</p><a href="#">詳しくみる ›</a></article>
    <article class="post"><div class="photo" role="img" aria-label="白衣の歯科医師の写真"></div><p>開業準備で押さえておきたいポイントをまとめました。</p><a href="#">詳しくみる ›</a></article>
    <article class="post"><div class="photo" role="img" aria-label="握手を交わす手元の写真"></div><p>クライアント医院との新しい取り組みが始まりました。</p><a href="#">詳しくみる ›</a></article>
    <article class="post"><div class="photo" role="img" aria-label="会議室で話す男性の写真"></div><p>歯科塾の次回開催日と内容についてお知らせします。</p><a href="#">詳しくみる ›</a></article>
  </div>
  <div class="pager">
    <i><svg width="10" height="10" viewBox="0 0 10 10"><path d="M7 1L3 5l4 4" stroke="#fff" fill="none" stroke-width="1.5"/></svg></i>
    <span class="on"></span><span></span><span></span><span></span><span></span>
    <i><svg width="10" height="10" viewBox="0 0 10 10"><path d="M3 1l4 4-4 4" stroke="#fff" fill="none" stroke-width="1.5"/></svg></i>
  </div>
</section>

<section class="recruit">
  <div class="photo" role="img" aria-label="微笑むスーツ姿の女性の写真"></div>
  <div class="recruit-body">
    <div class="sec-head"><small>RECRUIT</small><h2>採用情報</h2></div>
    <p class="lead">一緒に「<em>楽</em>」ぼう！<br>あなたが動けば、世界も動きだす。</p>
    <p>歯科医院専門の経営コンサルティングを手掛ける私たちは、<br>医院の成長を支えることで地域の健康を守っています。<br>変化を楽しみ、自ら考えて動ける仲間を探しています。<br>経験の有無は問いません。まずは気軽にお話ししましょう。</p>
    <a class="btn btn-wide" href="#">採用情報をみる<span>›</span></a>
  </div>
</section>

<section class="message">
  <div class="photo" role="img" aria-label="手を差し伸べるスーツ姿の男性の写真"></div>
  <h2>「困っている人を助けたい」<br>そんな想いでメドウパスは始まった</h2>
</section>

<section class="map" role="img" aria-label="事務所周辺の地図">
  <svg class="map-pin" width="28" height="40" viewBox="0 0 28 40"><path d="M14 0C6 0 0 6 0 14c0 10 14 26 14 26s14-16 14-26C28 6 22 0 14 0z" fill="#8a6aa6"/><circle cx="14" cy="14" r="5" fill="#fff"/></svg>
</section>

<footer class="site-footer">
  <div class="foot-brand"><span class="brand-mark"></span><span class="brand-name">Meadowpath</span></div>
  <nav class="foot-nav">
    <ul><li>会社概要</li><li class="sub">理念</li><li class="sub">代表挨拶</li></ul>
    <ul><li>サービス</li><li class="sub">コンサルティング</li><li class="sub">ホームページ作成</li><li class="sub">歯科塾</li></ul>
    <ul><li>クライアントの声</li></ul>
    <ul><li>歯科塾</li></ul>
    <ul><li>採用情報</li></ul>
    <ul><li>お問い合わせ</li></ul>
    <ul><li>ブログ</li></ul>
  </nav>
  <p class="foot-addr">〒000-0000<br>東京都架空区草原町1丁目2番3号 メドウパスビル5階<br>Copyright © Meadowpath Inc. All Rights Reserved.</p>
</footer>

</body>
</html>
```